Bref créative
Corvaxa of NYC
Stationary and Cards
Professional
Dale Fontanova
General Manager
42 Garrow Ave
Brookhollow NY 66431
1800 KORV NYC
dale.fontanova@corvaxanyc.com
Logo
www.corvaxanyc.com

```html
<!DOCTYPE html>
<html lang="en">
<head>
<meta charset="utf-8">
<title>Corvaxa of NYC — Stationery and Cards</title>
<link rel="stylesheet" href="https://fonts.googleapis.com/css2?family=Roboto:wght@400;700;900&display=swap">
<style>
  :root{
    --stage:#3b3f45;
    --paper:#ffffff;
    --brand-red:#c61f2a;
    --brand-navy:#1c3c8c;
    --ink:#3a3a3a;
    --muted:#8a8f96;
    --sky-top:#ffffff;
    --sky-bottom:#d9e6f3;
    --shadow:rgba(0,0,0,.45);
  }
  *{box-sizing:border-box;margin:0;padding:0}
  html,body{width:1200px;height:310px;overflow:hidden}
  body{background:var(--stage);font-family:"Roboto",Arial,sans-serif;color:var(--ink);position:relative}
  .piece{position:absolute;background:var(--paper);box-shadow:0 2px 6px var(--shadow);overflow:hidden}
  .wordmark{display:flex;align-items:center;gap:4px;font-weight:900;color:var(--brand-red);line-height:1;white-space:nowrap}
  .wordmark .mark{background:var(--brand-navy);flex:none}
  .skyline{position:absolute;left:0;right:0;bottom:0;background:linear-gradient(var(--sky-top),var(--sky-bottom))}
  .tiny{font-size:4px;line-height:6px;color:var(--muted)}

  /* presentation label */
  .intro{position:absolute;left:14px;top:12px}
  .intro .wordmark{font-size:13px}
  .intro .wordmark .mark{width:14px;height:14px}
  .intro .label{font-size:6px;color:#c9ccd1;margin-top:14px;margin-left:18px}

  /* business cards */
  .card{width:120px;height:62px;padding:7px}
  .card .wordmark{font-size:7px}
  .card .wordmark .mark{width:7px;height:7px}
  .card .details{margin-top:8px}
  .card .name{font-size:5px;font-weight:700;color:var(--ink);line-height:7px}
  .card-front{left:12px;top:118px}
  .card-back{left:144px;top:118px}
  .card-plain{left:12px;top:210px}
  .card-plain .skyline{height:26px}
  .card-red{left:144px;top:210px;background:var(--brand-red)}
  .card-red .wordmark{color:var(--paper);font-size:8px;justify-content:center;margin-top:18px}
  .card-red .wordmark .mark{background:var(--paper);width:8px;height:8px}

  /* letterheads */
  .letterhead{width:192px;height:272px;top:12px;padding:12px}
  .letterhead.first{left:276px}
  .letterhead.second{left:492px}
  .letterhead .head{display:flex;justify-content:space-between;align-items:flex-start}
  .letterhead .wordmark{font-size:9px}
  .letterhead .wordmark .mark{width:9px;height:9px}
  .letterhead .contact{text-align:right}
  .letterhead .skyline{height:90px}
  .letterhead .foot{position:absolute;bottom:6px;left:0;right:0;text-align:center}

  /* compliment slip and card */
  .slip{left:696px;width:192px}
  .slip.tall{top:43px;height:137px;padding:10px}
  .slip.short{top:204px;height:80px}
  .slip .wordmark{font-size:8px}
  .slip .wordmark .mark{width:8px;height:8px}
  .slip.tall .skyline{height:48px}
  .slip.short .skyline{height:56px}

  /* envelopes */
  .envelope{left:907px;width:282px;height:72px}
  .envelope svg{position:absolute;inset:0}
  .envelope.navy{top:48px;background:var(--brand-navy)}
  .envelope.red-flap{top:130px}
  .envelope.plain{top:214px}
  .envelope .seal{position:absolute;left:133px;width:16px;height:16px;background:var(--paper);border-radius:50%}
  .envelope.navy .seal{top:30px}
  .envelope.red-flap .seal{top:30px}
</style>
</head>
<body>

  <div class="intro">
    <div class="wordmark"><span class="mark"></span>Corvaxa of NYC</div>
    <div class="label">Stationery Concept</div>
  </div>

  <!-- business cards -->
  <section class="piece card card-front">
    <div class="wordmark"><span class="mark"></span>Corvaxa of NYC</div>
    <div class="details">
      <div class="name">Dale Fontanova</div>
      <div class="tiny">General Manager</div>
      <div class="tiny">42 Garrow Ave, Brookhollow NY 66431</div>
      <div class="tiny">1800 KORV NYC</div>
    </div>
  </section>
  <section class="piece card card-back">
    <div class="wordmark"><span class="mark"></span>Corvaxa of NYC</div>
    <div class="details">
      <div class="tiny">dale.fontanova@corvaxanyc.com</div>
      <div class="tiny">www.corvaxanyc.com</div>
      <div class="tiny">1800 KORV NYC</div>
    </div>
  </section>
  <section class="piece card card-plain">
    <div class="wordmark"><span class="mark"></span>Corvaxa of NYC</div>
    <div class="skyline" role="img" aria-label="Faint New York city skyline"></div>
  </section>
  <section class="piece card card-red">
    <div class="wordmark"><span class="mark"></span>Corvaxa of NYC</div>
  </section>

  <!-- letterheads -->
  <section class="piece letterhead first">
    <div class="head">
      <div class="wordmark"><span class="mark"></span>Corvaxa of NYC</div>
      <div class="contact tiny">
        42 Garrow Ave<br>Brookhollow NY 66431<br>1800 KORV NYC<br>www.corvaxanyc.com
      </div>
    </div>
    <div class="skyline" role="img" aria-label="Faint New York city skyline"></div>
    <div class="foot tiny">www.corvaxanyc.com</div>
  </section>
  <section class="piece letterhead second">
    <div class="skyline" role="img" aria-label="Faint New York city skyline"></div>
    <div class="foot tiny">www.corvaxanyc.com</div>
  </section>

  <!-- compliment pieces -->
  <section class="piece slip tall">
    <div class="wordmark"><span class="mark"></span>Corvaxa of NYC</div>
    <div class="skyline" role="img" aria-label="Faint New York city skyline"></div>
  </section>
  <section class="piece slip short">
    <div class="skyline" role="img" aria-label="Faint New York city skyline"></div>
  </section>

  <!-- envelopes -->
  <section class="piece envelope navy">
    <svg viewBox="0 0 282 72" preserveAspectRatio="none" aria-hidden="true">
      <path d="M0 0 L141 40 L282 0" fill="none" stroke="#15306f" stroke-width="2"/>
    </svg>
    <span class="seal"></span>
  </section>
  <section class="piece envelope red-flap">
    <svg viewBox="0 0 282 72" preserveAspectRatio="none" aria-hidden="true">
      <path d="M0 0 L282 0 L141 40 Z" fill="var(--brand-red)"/>
    </svg>
    <span class="seal" style="background:var(--brand-navy)"></span>
  </section>
  <section class="piece envelope plain">
    <svg viewBox="0 0 282 72" preserveAspectRatio="none" aria-hidden="true">
      <path d="M0 0 L141 40 L282 0 M0 72 L120 34 M282 72 L162 34" fill="none" stroke="#dde1e6" stroke-width="1"/>
    </svg>
  </section>

</body>
</html>
```